Business Card Design

We have our logo and everything in place. Looking to have a layout for our new business cards designed. These will be printed with a matte finish, possibly rounded corners, and looking to incorporate some cool spot UV layers into the design.

Ive uploaded the existing card front and back as well as our logo.

Card Size Will Be 3.5" x 2"

Industry/Entity Type

Business

```html
<!DOCTYPE html>
<html lang="en">
<head>
<meta charset="utf-8">
<title>Ridgeline Deck and Rail – Business Card</title>
<link rel="stylesheet" href="https://fonts.googleapis.com/css2?family=Open+Sans:wght@400;600&display=swap">
<style>
  :root {
    --stage: #e9e7e4;
    --card-black: #0f0f0f;
    --card-black-2: #1c1c1c;
    --ink-light: #ffffff;
    --ink-dark: #1a1a1a;
    --panel-top: #ffffff;
    --panel-mid: #c9c9c9;
    --panel-low: #7a7a7a;
    --panel-bottom: #2a2a2a;
  }
  * { margin: 0; padding: 0; box-sizing: border-box; }
  html, body { width: 1200px; height: 900px; overflow: hidden; }
  body {
    background: var(--stage);
    font-family: "Open Sans", Arial, sans-serif;
    position: relative;
  }
  .card {
    position: absolute;
    border-radius: 14px;
    overflow: hidden;
    background: radial-gradient(ellipse at 40% 30%, var(--card-black-2), var(--card-black));
    box-shadow: 0 6px 18px rgba(0,0,0,0.25);
  }
  .card-front { left: 78px; top: 35px; width: 587px; height: 360px; }
  .card-back  { left: 390px; top: 507px; width: 565px; height: 348px; }

  .front-panel { position: absolute; inset: 0; }

  .brand-name {
    position: absolute;
    color: var(--ink-light);
    font-weight: 600;
    white-space: nowrap;
  }
  .card-front .brand-name { left: 36px; top: 66px; font-size: 28px; }
  .card-back .brand-name {
    left: 0; right: 0; top: 156px;
    text-align: center; font-size: 40px;
  }

  .contact {
    position: absolute;
    left: 0; right: 0;
    text-align: center;
    color: var(--ink-dark);
    font-weight: 600;
  }
  .person-name { top: 204px; font-size: 20px; }
  .person-role { top: 232px; font-size: 16px; }
  .contact-list {
    position: absolute; left: 0; right: 0; top: 272px;
    list-style: none; text-align: center;
    color: var(--ink-light); font-size: 16.5px; font-weight: 600;
    line-height: 24px;
  }
  .contact-list li { display: block; white-space: nowrap; }
  .contact-list svg { width: 12px; height: 12px; margin-right: 6px; vertical-align: -1px; fill: var(--ink-light); }
</style>
</head>
<body>

<section class="card card-front">
  <svg class="front-panel" viewBox="0 0 587 360" width="587" height="360" aria-hidden="true">
    <defs>
      <linearGradient id="panel-shade" x1="0" y1="0" x2="0" y2="1">
        <stop offset="0" stop-color="#ffffff"/>
        <stop offset="0.45" stop-color="#c9c9c9"/>
        <stop offset="0.75" stop-color="#7a7a7a"/>
        <stop offset="1" stop-color="#2a2a2a"/>
      </linearGradient>
    </defs>
    <polyline points="0,268 294,135 587,272" fill="none" stroke="#ffffff" stroke-width="9"/>
    <polygon points="0,288 294,152 587,292 587,360 0,360" fill="url(#panel-shade)"/>
  </svg>

  <div class="brand-name">Ridgeline Deck and Rail</div>

  <p class="contact person-name">Daniel Carver</p>
  <p class="contact person-role">President</p>

  <ul class="contact-list">
    <li><svg viewBox="0 0 24 24"><path d="M6.6 10.8a15.1 15.1 0 0 0 6.6 6.6l2.2-2.2a1 1 0 0 1 1-.25 11.4 11.4 0 0 0 3.6.57 1 1 0 0 1 1 1V20a1 1 0 0 1-1 1A17 17 0 0 1 3 4a1 1 0 0 1 1-1h3.5a1 1 0 0 1 1 1c0 1.25.2 2.45.57 3.57a1 1 0 0 1-.25 1z"/></svg>555.010.7316</li>
    <li><svg viewBox="0 0 24 24"><path d="M2 5h20v14H2z M2 5l10 8 10-8" stroke="#1a1a1a" stroke-width="1.5"/></svg>ridgelinedeckandrail@mailbox.com</li>
    <li><svg viewBox="0 0 24 24"><circle cx="12" cy="12" r="10"/></svg>www.ridgelinedeckandrail.com</li>
  </ul>
</section>

<section class="card card-back">
  <div class="brand-name">Ridgeline Deck and Rail</div>
</section>

</body>
</html>
```